www.varnolinkgroup.com Redesign

The current website was designed 2 - 3 years ago, and we feel it is a bit outdated and bland. We would like to get a new design implement, which is fresh and shows our business/network in a professional manner.

It is important for the site to emphasize that we are a European specialist in our market, Specialist logistics, so we would very much like this emphasized with a European map feature on the main page.

Open to suggestions on how this is done, and appreciate your efforts.

Please visit our existing website at www.varnolinkgroup.com to understand more about the business to aide the design.

I have loads more images should you want more to look at, you may need the rest of the data when the rest of the pages are designed etc.

Target Market(s)

We provide speclist logistics / freight services to a host of industries including but not limited to - HealthCare, Banking & Retail, Vending & Gaming, Fitness, Access Control, Power, Data and Office print. So we need to show diversity and that we can flex to customer needs.

Industry/Entity Type

Logistics

Font styles to use
Sans Serif

Colors
0555a3
34a7d8
959595
ffffff

Requirements
Must have
• - European Map emphasizing European capabilities
• - On each partner page a smaller version of the European map showing the countries they cover (this info is shown in the text provided)
• - Business sectors brief similar to current website on opening page showing industries we support (dont have to use provided logos - happy for you to provide new content)
• - Must be an easy link on each and every page for the customer to click and submit an inquiry (info@varnolinkgroup.com)
Nice to have
• - Interactive European Map - so the user can click on the country and it takes them to the service partners page that managers that country. ie - if they click on UK it takes them to the UK Partner = Morvath Kellisto UK
• - Clean site not too busy
• - Prefer to have larger images and less text
Should not have
• - Too much white - unless you can keep it fresh (Current website design has lots of white background and looks bland)

```html
<!DOCTYPE html>
<html lang="en">
<head>
<meta charset="utf-8">
<title>Varnolink — Technical Logistics Network</title>
<link rel="stylesheet" href="https://fonts.googleapis.com/css2?family=Roboto:wght@400;500;700&family=Open+Sans:wght@400;600;700&display=swap">
<style>
:root{
  --blue:#0555a3;
  --blue-deep:#0a3f86;
  --sky:#34a7d8;
  --accent:#1d6fe0;
  --grey:#959595;
  --ink:#333a40;
  --logo-ink:#34495e;
  --white:#ffffff;
}
*{box-sizing:border-box;margin:0;padding:0}
html,body{width:1200px;height:3622px;overflow:hidden;background:var(--white)}
body{position:relative;font-family:"Open Sans",Arial,sans-serif;color:var(--ink)}
.abs{position:absolute}

/* header */
.site-header{left:0;top:0;width:1200px;height:109px;background:var(--white);z-index:2}
.brand{display:flex;align-items:center;gap:12px;font-family:"Roboto",Arial,sans-serif;font-weight:700;font-size:40px;color:var(--logo-ink);letter-spacing:1px}
.brand-dot{width:30px;height:30px;border-radius:50%;background:var(--blue)}
.site-header .brand{position:absolute;left:98px;top:32px}
.main-nav{position:absolute;left:424px;top:0;height:109px;display:flex}
.main-nav a{display:block;padding:46px 10px 0;height:109px;font-family:"Roboto",Arial,sans-serif;font-size:17px;color:#222;text-decoration:none}
.main-nav a.active{color:var(--accent);border-bottom:4px solid var(--accent)}

/* hero */
.hero{left:0;top:109px;width:1200px;height:557px;background:linear-gradient(100deg,#7a6a4d 0%,#8a7a5c 22%,#3b5f97 45%,#2a5aa8 70%,#5b7fb8 100%)}
.hero-title{left:0;top:312px;width:1200px;text-align:center;color:var(--white);font-family:"Roboto",Arial,sans-serif;font-weight:500;font-size:49px;line-height:60px;letter-spacing:2px}
.hero-sub{left:0;top:370px;width:1200px;text-align:center;color:var(--white);font-family:"Roboto",Arial,sans-serif;font-weight:500;font-size:32px;line-height:40px}
.btn-ghost{border:2px solid var(--white);color:var(--white);font-family:"Roboto",Arial,sans-serif;font-size:17px;display:flex;align-items:center;justify-content:center;text-decoration:none}
.hero-btn{left:506px;top:434px;width:164px;height:44px}
.dots{left:557px;top:620px;display:flex;gap:10px}
.dots span{width:11px;height:11px;border-radius:50%;background:var(--white)}
.dots span.on{box-shadow:0 0 0 3px rgba(255,255,255,.5)}

/* about */
.about-map{left:109px;top:690px;width:458px;height:420px;border-radius:50%;background:radial-gradient(circle at 45% 45%,#e6e8ea 0%,#d5d8db 45%,#f4f5f6 72%,#ffffff 100%)}
.about-title{left:602px;top:745px;font-family:"Roboto",Arial,sans-serif;font-weight:500;font-size:36px;line-height:44px;color:var(--ink)}
.about-title b{color:var(--accent);font-weight:500}
.about-text{left:603px;top:808px;width:500px;font-size:14px;line-height:24px;color:#4a4f55}
.about-text p{margin-bottom:12px}
.btn-outline{left:603px;top:1002px;width:147px;height:38px;border:2px solid var(--blue);color:var(--blue);font-family:"Roboto",Arial,sans-serif;font-weight:700;font-size:15px;display:flex;align-items:center;justify-content:center}

/* services */
.services{left:0;top:1075px;width:1200px;height:542px;background:linear-gradient(180deg,#1f63b8 0%,#2b78cc 50%,#2a6fc4 100%)}
.section-title{font-family:"Roboto",Arial,sans-serif;font-weight:500;font-size:30px;line-height:36px;text-align:center;width:1200px;left:0}
.services .section-title{top:124px;color:var(--white)}
.service{width:288px;height:288px;border-radius:50%;border:3px solid rgba(255,255,255,.75);text-align:center;color:var(--white);padding-top:58px}
.service.dark{background:var(--blue-deep)}
.service.light{background:#1a86d1}
.service h3{font-family:"Roboto",Arial,sans-serif;font-weight:500;font-size:20px;margin-top:10px}
.service p{font-size:10.5px;line-height:14px;width:190px;margin:8px auto 0;opacity:.85}
.service .btn-ghost{width:110px;height:30px;font-size:11px;margin:10px auto 0;border-width:1.5px}

/* sectors */
.sectors-title{top:1662px;color:#2b2b2b;font-weight:400;font-size:28px}
.sector{width:190px;text-align:center}
.sector-badge{width:96px;height:96px;border-radius:50%;background:var(--blue);margin:0 auto;border:4px solid #d6e3f2;display:flex;align-items:center;justify-content:center}
.sector span{display:block;margin-top:18px;font-family:"Roboto",Arial,sans-serif;font-weight:500;font-size:14.5px;color:#2b2b2b}

/* banner */
.banner{left:0;top:1953px;width:1200px;height:323px;background:linear-gradient(90deg,#5b6b5d 0%,#3a4a5a 35%,#2c3e58 60%,#4f5f6c 100%)}
.banner-title{left:0;top:2045px;width:1200px;text-align:center;color:var(--white);font-family:"Roboto",Arial,sans-serif;font-weight:500;font-size:31px;line-height:39px}
.banner-btn{left:508px;top:2147px;width:182px;height:42px;font-size:15px}

/* news */
.news-title{left:101px;top:2326px;font-family:"Roboto",Arial,sans-serif;font-weight:500;font-size:29px;line-height:36px;color:var(--accent)}
.news-card{width:314px;height:360px;border:1px solid #d8d8d8;background:var(--white);text-align:center}
.news-img{width:100%;height:205px}
.news-date{position:absolute;left:90px;top:187px;width:134px;height:34px;background:var(--sky);color:var(--white);font-size:14px;display:flex;align-items:center;justify-content:center}
.news-card h4{margin-top:30px;font-family:"Roboto",Arial,sans-serif;font-weight:500;font-size:19px;color:var(--blue)}
.news-card p{font-size:11.5px;line-height:16px;color:#555;width:260px;margin:8px auto 0}
.news-card .more{display:block;margin-top:10px;font-family:"Roboto",Arial,sans-serif;font-weight:700;font-size:12.5px;color:#222}

/* contact */
.contact{left:0;top:2747px;width:1200px;height:430px;background:linear-gradient(180deg,#2a7fd0 0%,#2672c6 60%,#1f66b8 100%)}
.contact .section-title{top:128px;color:var(--white);font-weight:400;font-size:29px}
.field{background:var(--white);color:#444;font-size:15px;padding:10px 16px}
.submit{background:var(--blue-deep);color:var(--white);font-family:"Roboto",Arial,sans-serif;font-weight:700;font-size:17px;display:flex;align-items:center;justify-content:center}

/* footer */
.site-footer{left:0;top:3150px;width:1200px;height:472px;background:var(--grey)}
.site-footer .brand{position:absolute;left:100px;top:160px;color:#3d4a55}
.foot-about{left:113px;top:236px;width:240px;font-size:12px;line-height:17px;color:var(--white)}
.foot-col{color:var(--white)}
.foot-col h5{font-family:"Roboto",Arial,sans-serif;font-weight:500;font-size:21px;padding-bottom:8px;border-bottom:1px solid rgba(255,255,255,.35);width:140px}
.foot-col ul{list-style:none;margin-top:12px}
.foot-col li{font-size:14px;line-height:31px}
.contact-line{display:flex;align-items:center;gap:10px;font-size:14px;line-height:31px;white-space:nowrap}
.socials{left:802px;top:313px;display:flex;gap:12px}
.socials span{width:38px;height:38px;border-radius:50%;background:var(--white)}
.foot-rule{left:85px;top:403px;width:1030px;height:1px;background:rgba(255,255,255,.35)}
.copyright{left:0;top:426px;width:1200px;text-align:center;font-size:14px;color:#eaeaea}
</style>
</head>
<body>

<header class="site-header abs">
  <div class="brand"><span class="brand-dot"></span>VARNOLINK</div>
  <nav class="main-nav">
    <a class="active" href="#">HOME</a>
    <a href="#">ABOUT US</a>
    <a href="#">BUSINESS SECTORS</a>
    <a href="#">SERVICES</a>
    <a href="#">NETWORK</a>
    <a href="#">CONTACT US</a>
  </nav>
</header>

<div class="hero abs" role="img" aria-label="Warehouse worker in a high-visibility vest handling parts beside blue storage bins"></div>
<h1 class="hero-title abs">THE LEADING GLOBAL NETWORK</h1>
<p class="hero-sub abs">FOR HIGH TECH SERVICES &amp; LOGISTICS</p>
<a class="btn-ghost hero-btn abs" href="#">READ MORE</a>
<div class="dots abs"><span class="on"></span><span></span><span></span><span></span></div>

<div class="about-map abs" role="img" aria-label="Dotted world map illustration highlighting network locations"></div>
<h2 class="about-title abs">ABOUT <b>VARNOLINK</b></h2>
<div class="about-text abs">
  <p>Varnolink leads the way in specialist technical logistics. Having identified the best in class partners and established exclusive relationships with these companies, Varnolink work to deliver the following core values;</p>
  <p>With each partner you benefit from the expertise, competitive advantage, service and a local presence, whilst being able to enjoy the benefit of a consistent high service level across the countries</p>
</div>
<a class="btn-outline abs" href="#">READ MORE</a>

<section class="services abs" aria-label="Our services">
  <svg class="abs" style="left:0;top:0" width="1200" height="90" viewBox="0 0 1200 90">
    <path d="M0 0 H1200 V5 L600 80 L0 5 Z" fill="#ffffff"/>
    <path d="M0 14 L600 89 L1200 14" fill="none" stroke="#ffffff" stroke-width="2" opacity=".7"/>
  </svg>
  <h2 class="section-title abs">OUR SERVICES</h2>

  <div class="service dark abs" style="left:88px;top:185px">
    <svg width="80" height="56" viewBox="0 0 80 56" fill="none" stroke="#fff" stroke-width="3"><rect x="4" y="6" width="44" height="34"/><path d="M48 18 H64 L74 30 V40 H48"/><circle cx="18" cy="44" r="6" fill="#0a3f86"/><circle cx="62" cy="44" r="6" fill="#0a3f86"/></svg>
    <h3>Transport</h3>
    <p>Sed ut perspiciatis unde omnis iste natus error sit voluptatem</p>
    <div class="btn-ghost">READ MORE</div>
  </div>
  <div class="service light abs" style="left:332px;top:185px">
    <svg width="80" height="56" viewBox="0 0 80 56" fill="none" stroke="#fff" stroke-width="3"><path d="M40 4 L64 14 V40 L40 52 L16 40 V14 Z"/><path d="M16 14 L40 26 L64 14 M40 26 V52"/></svg>
    <h3>Warehousing</h3>
    <p>Sed ut perspiciatis unde omnis iste natus error sit voluptatem</p>
    <div class="btn-ghost">READ MORE</div>
  </div>
  <div class="service dark abs" style="left:578px;top:185px">
    <svg width="80" height="56" viewBox="0 0 80 56" fill="none" stroke="#fff" stroke-width="3"><circle cx="40" cy="28" r="10"/><path d="M40 6 V14 M40 42 V50 M18 28 H26 M54 28 H62 M24 12 L30 18 M50 38 L56 44 M56 12 L50 18 M30 38 L24 44"/></svg>
    <h3>Technical Services</h3>
    <p>Sed ut perspiciatis unde omnis iste natus error sit voluptatem</p>
    <div class="btn-ghost">READ MORE</div>
  </div>
  <div class="service light abs" style="left:822px;top:185px">
    <svg width="80" height="56" viewBox="0 0 80 56" fill="none" stroke="#fff" stroke-width="3"><rect x="18" y="4" width="44" height="48"/><path d="M18 16 H62"/><path d="M50 34 H32 M38 28 L32 34 L38 40"/></svg>
    <h3>Returns</h3>
    <p>Sed ut perspiciatis unde omnis iste natus error sit voluptatem</p>
    <div class="btn-ghost">READ MORE</div>
  </div>
</section>

<h2 class="section-title sectors-title abs">BUSINESS SECTORS</h2>
<svg class="abs" style="left:88px;top:1766px" width="28" height="48" viewBox="0 0 28 48"><path d="M24 2 L4 24 L24 46" fill="none" stroke="#555" stroke-width="2"/></svg>
<svg class="abs" style="left:1090px;top:1776px" width="28" height="48" viewBox="0 0 28 48"><path d="M4 2 L24 24 L4 46" fill="none" stroke="#555" stroke-width="2"/></svg>

<div class="sector abs" style="left:110px;top:1738px">
  <div class="sector-badge"><svg width="44" height="44" viewBox="0 0 44 44" fill="none" stroke="#fff" stroke-width="3"><path d="M18 6 L26 6 L26 24 L18 24 Z M22 24 V30 M10 38 H34 M14 30 H30"/></svg></div>
  <span>HEALTHTECH</span>
</div>
<div class="sector abs" style="left:306px;top:1738px">
  <div class="sector-badge"><svg width="44" height="44" viewBox="0 0 44 44" fill="none" stroke="#fff" stroke-width="3"><circle cx="22" cy="10" r="5"/><path d="M22 15 V28"/><rect x="8" y="28" width="28" height="10" rx="3"/></svg></div>
  <span>VENDING &amp; GAMING</span>
</div>
<div class="sector abs" style="left:499px;top:1738px">
  <div class="sector-badge"><svg width="44" height="44" viewBox="0 0 44 44" fill="none" stroke="#fff" stroke-width="3"><rect x="8" y="4" width="28" height="36"/><rect x="14" y="10" width="16" height="10"/><path d="M14 28 H30 M14 34 H24"/></svg></div>
  <span>BANKING &amp; RETAIL</span>
</div>
<div class="sector abs" style="left:694px;top:1738px">
  <div class="sector-badge"><svg width="44" height="44" viewBox="0 0 44 44" fill="none" stroke="#fff" stroke-width="3"><path d="M4 14 H40 M8 8 V20 M36 8 V20"/><circle cx="22" cy="22" r="4"/><path d="M22 26 V34 M16 40 L22 34 L28 40"/></svg></div>
  <span>FITNESS</span>
</div>
<div class="sector abs" style="left:890px;top:1738px">
  <div class="sector-badge"><svg width="44" height="44" viewBox="0 0 44 44" fill="none" stroke="#fff" stroke-width="3"><rect x="6" y="8" width="32" height="28"/><path d="M22 8 V36"/><circle cx="18" cy="22" r="1.5" fill="#fff"/></svg></div>
  <span>ACCESS CONTROL</span>
</div>

<div class="banner abs" role="img" aria-label="Technician servicing an equipment cabinet outside an office building"></div>
<h2 class="banner-title abs">VARNOLINK PROVIDE ADVANCED TECHNICAL<br>LOGISTICS SERVICES</h2>
<a class="btn-ghost banner-btn abs" href="#">OUR SERVICES</a>

<h2 class="news-title abs">LATEST NEWS</h2>
<article class="news-card abs" style="left:97px;top:2385px">
  <div class="news-img" role="img" aria-label="Delivery truck being loaded with boxed equipment" style="background:linear-gradient(160deg,#9aa3ab,#5d6670)"></div>
  <div class="news-date">20 Aug 2017</div>
  <h4>Praesent elementum elit</h4>
  <p>netus et malesuada fames ac turpis egestas Cras id elit Integer quis urna Ut ante enim dapibus malesuada fringilla eu cond</p>
  <span class="more">READ MORE</span>
</article>
<article class="news-card abs" style="left:442px;top:2385px">
  <div class="news-img" role="img" aria-label="Trailer interior stacked with wrapped pallets" style="background:linear-gradient(160deg,#3a5d9c,#8a8f96)"></div>
  <div class="news-date">05 Aug 2017</div>
  <h4>Maecenas aliquet velit</h4>
  <p>netus et malesuada fames ac turpis egestas Cras id elit Integer quis urna Ut ante enim dapibus malesuada fringilla eu cond</p>
  <span class="more">READ MORE</span>
</article>
<article class="news-card abs" style="left:787px;top:2385px">
  <div class="news-img" role="img" aria-label="Two engineers moving a medical scanner unit" style="background:linear-gradient(160deg,#d9dbdd,#8c9096)"></div>
  <div class="news-date">01 Aug 2017</div>
  <h4>Nunc tempus felis vita</h4>
  <p>netus et malesuada fames ac turpis egestas Cras id elit Integer quis urna Ut ante enim dapibus malesuada fringilla eu cond</p>
  <span class="more">READ MORE</span>
</article>

<section class="contact abs" aria-label="Get in touch">
  <svg class="abs" style="left:570px;top:0" width="60" height="18" viewBox="0 0 60 18"><path d="M0 0 H60 L30 16 Z" fill="#ffffff"/></svg>
  <h2 class="section-title abs">GET IN TOUCH</h2>
  <div class="field abs" style="left:222px;top:193px;width:370px;height:44px">Your Name</div>
  <div class="field abs" style="left:222px;top:249px;width:370px;height:43px">Email address</div>
  <div class="field abs" style="left:222px;top:304px;width:370px;height:46px">Phone</div>
  <div class="field abs" style="left:601px;top:193px;width:369px;height:102px">Message</div>
  <div class="submit abs" style="left:601px;top:304px;width:369px;height:46px">SUBMIT NOW</div>
</section>

<footer class="site-footer abs">
  <svg class="abs" style="left:0;top:0" width="1200" height="80" viewBox="0 0 1200 80">
    <path d="M0 0 H1200 V10 Q600 80 0 10 Z" fill="#1f66b8"/>
    <path d="M0 22 Q600 92 1200 22" fill="none" stroke="#ffffff" stroke-width="2" opacity=".8"/>
  </svg>
  <div class="brand"><span class="brand-dot" style="background:#3d4a55"></span>VARNOLINK</div>
  <p class="foot-about abs">Aociisqu ad litora torquent per conubia nostra per inceptos hyme naeos Proin nulla arcu nonummy</p>

  <div class="foot-col abs" style="left:401px;top:150px">
    <h5>Company</h5>
    <ul><li>Home</li><li>About us</li><li>Sector Areas</li><li>Services</li></ul>
  </div>
  <div class="foot-col abs" style="left:604px;top:150px">
    <h5>Resources</h5>
    <ul><li>Support</li><li>Nework</li><li>News</li><li>Contact Us</li></ul>
  </div>
  <div class="foot-col abs" style="left:809px;top:150px">
    <h5 style="border:none">Contact Us</h5>
    <div style="margin-top:4px">
      <div class="contact-line"><svg width="16" height="20" viewBox="0 0 16 20"><path d="M8 1 C4 1 1 4 1 8 C1 13 8 19 8 19 C8 19 15 13 15 8 C15 4 12 1 8 1 Z" fill="#fff"/><circle cx="8" cy="8" r="2.5" fill="#959595"/></svg>42 Harrow Lane, Suite 7, Leeds LS1 4QP</div>
      <div class="contact-line"><svg width="16" height="16" viewBox="0 0 16 16"><path d="M3 1 L6 1 L7 5 L5 6.5 C6 9 7 10 9.5 11 L11 9 L15 10 L15 13 C15 14 14 15 13 15 C6 15 1 10 1 3 C1 2 2 1 3 1 Z" fill="none" stroke="#fff" stroke-width="1.4"/></svg>555.014.3380</div>
      <div class="contact-line"><svg width="18" height="14" viewBox="0 0 18 14"><rect x="1" y="1" width="16" height="12" fill="none" stroke="#fff" stroke-width="1.4"/><path d="M1 1 L9 8 L17 1" fill="none" stroke="#fff" stroke-width="1.4"/></svg>info@varnolinkgroup.com</div>
    </div>
  </div>
  <div class="socials abs" aria-hidden="true"><span></span><span></span><span></span><span></span><span></span></div>
  <div class="foot-rule abs"></div>
  <p class="copyright abs">© 2017 Company Name. All right reserved</p>
</footer>

</body>
</html>
```